card design for engineering consultancy

engineering drafting and project management company the provides drafting services for.
Electrical, Hydraulic, Mechanical, and Civil services
The company is called Q7R Services and logo is as attached
Information on card should be.
1. Logo
2.website : Q7RServices.example
3. email : info@Q7RServices.example
4. Phone: (+61) 400512836
5. Motto: Design - Document - Develop - Deliver

this card should be basically used for business identification only

Target Market(s)

electricians plumbers air conditioning installers and civil contractors

Industry/Entity Type

engineering, drafting, electrical, plumbing, airconditioning, civil

Contact Information for Business Card

1. Logo 2.website : Q7RServices.example 3. email : info@Q7RServices.example 4. Phone: (+61) 400512836 5. Motto: Design - Document - Develop - Deliver

Font styles to use
Serif

Requirements
Must have
• logo
Nice to have
• something inovative and different that makes it stand out from being just another business card

```html
<!DOCTYPE html>
<html lang="en">
<head>
<meta charset="utf-8">
<title>Q7R Services — Business Card</title>
<link rel="stylesheet" href="https://fonts.googleapis.com/css2?family=Exo+2:wght@400;600&display=swap">
<style>
  :root {
    --backdrop: #e4e3e1;
    --card: #262626;
    --card-deep: #1c1c1c;
    --accent: #d3202f;
    --ink: #ffffff;
    --ink-soft: #e8e8e8;
    --font-text: "Exo 2", sans-serif;
  }
  * { box-sizing: border-box; margin: 0; padding: 0; }
  html, body {
    width: 1200px;
    height: 801px;
    overflow: hidden;
  }
  body {
    background: var(--backdrop);
    font-family: var(--font-text);
    position: relative;
  }
  .card {
    position: absolute;
    top: 244px;
    width: 540px;
    height: 312px;
    background: var(--card);
    border-bottom: 6px solid var(--accent);
    overflow: hidden;
  }
  .card--front { left: 40px; }
  .card--back { left: 620px; }

  /* Front */
  .brand {
    position: absolute;
    display: flex;
    align-items: center;
    gap: 12px;
    color: var(--ink);
    font-weight: 600;
    letter-spacing: 0.06em;
    text-transform: uppercase;
  }
  .brand__square {
    width: 22px;
    height: 22px;
    background: var(--accent);
    flex: none;
  }
  .card--front .brand {
    left: 38px;
    top: 112px;
    font-size: 24px;
  }
  .divider {
    position: absolute;
    left: 262px;
    top: 78px;
    width: 1px;
    height: 110px;
    background: var(--accent);
    opacity: 0.8;
  }
  .contacts {
    position: absolute;
    left: 284px;
    top: 84px;
    list-style: none;
    display: flex;
    flex-direction: column;
    gap: 16px;
  }
  .contacts__item {
    display: flex;
    align-items: center;
    gap: 10px;
    color: var(--ink-soft);
    font-size: 15px;
    letter-spacing: 0.02em;
  }
  .contacts__icon {
    width: 15px;
    height: 15px;
    flex: none;
    fill: var(--accent);
  }
  .motto {
    position: absolute;
    left: 38px;
    bottom: 40px;
    color: var(--ink-soft);
    font-size: 17px;
    letter-spacing: 0.03em;
  }

  /* Back */
  .back-field {
    position: absolute;
    inset: 0;
    background:
      linear-gradient(150deg, #3a3a3a 0%, #2a2a2a 45%, #1a1a1a 100%);
  }
  .card--back .brand {
    right: 34px;
    bottom: 44px;
    font-size: 20px;
  }
  .card--back .brand__square {
    width: 18px;
    height: 18px;
  }
</style>
</head>
<body>

  <section class="card card--front" aria-label="Business card front">
    <div class="brand">
      <span class="brand__square"></span>
      <span class="brand__name">Q7R Services</span>
    </div>

    <div class="divider"></div>

    <ul class="contacts">
      <li class="contacts__item">
        <svg class="contacts__icon" viewBox="0 0 24 24" aria-hidden="true">
          <path d="M6.6 10.8a15.1 15.1 0 0 0 6.6 6.6l2.2-2.2a1 1 0 0 1 1-.25 11.4 11.4 0 0 0 3.6.57 1 1 0 0 1 1 1V20a1 1 0 0 1-1 1A17 17 0 0 1 3 4a1 1 0 0 1 1-1h3.5a1 1 0 0 1 1 1c0 1.25.2 2.45.57 3.6a1 1 0 0 1-.25 1z"/>
        </svg>
        <span>(+61) 400512836</span>
      </li>
      <li class="contacts__item">
        <svg class="contacts__icon" viewBox="0 0 24 24" aria-hidden="true">
          <path d="M2 5h20v14H2z M3.5 6.5 12 13l8.5-6.5" fill="none" stroke="#d3202f" stroke-width="2"/>
        </svg>
        <span>info@Q7RServices.example</span>
      </li>
      <li class="contacts__item">
        <svg class="contacts__icon" viewBox="0 0 24 24" aria-hidden="true">
          <circle cx="12" cy="12" r="9" fill="none" stroke="#d3202f" stroke-width="2"/>
          <path d="M3 12h18M12 3c3 3 3 15 0 18M12 3c-3 3-3 15 0 18" fill="none" stroke="#d3202f" stroke-width="1.6"/>
        </svg>
        <span>www.Q7RServices.example</span>
      </li>
    </ul>

    <p class="motto">Design - Document - Develop - Deliver</p>
  </section>

  <section class="card card--back" aria-label="Business card back">
    <div class="back-field" role="img" aria-label="Decorative repeating brand pattern in dark and mid greys"></div>
    <div class="brand">
      <span class="brand__square"></span>
      <span class="brand__name">Q7R Services</span>
    </div>
  </section>

</body>
</html>
```